landscape and garden design business card

I would like a business card designed for my landscape and garden design company, Thistlecove Gardens. We are located in Colorado. I would like to include our logo, contact info, and social media/web site address or QR code. Looking for an organic, flowing design that incorporates our logo.

Target Market(s)

Homeowners and businesses that need garden and landscape design

Contact Information for Business Card

Would like it to say landscape and garden design

Requirements
Must have
• Landscape and garden design

```html
<!DOCTYPE html>
<html lang="en">
<head>
<meta charset="utf-8">
<title>Thistlecove Gardens — Business Card</title>
<link rel="stylesheet" href="https://fonts.googleapis.com/css2?family=Playfair+Display:wght@400;700&display=swap">
<style>
  :root {
    --forest: #032522;
    --stone: #bcbaab;
    --ink: #1d2a27;
    --backdrop: #3b3b3b;
    --rule: #5e625a;
  }
  * { margin: 0; padding: 0; box-sizing: border-box; }
  html, body {
    width: 1200px;
    height: 900px;
    overflow: hidden;
    background: var(--backdrop);
  }
  .canvas {
    position: relative;
    width: 1200px;
    height: 900px;
    font-family: "Playfair Display", Georgia, serif;
  }
  .card {
    position: absolute;
    top: 302px;
    width: 514px;
    height: 295px;
  }
  .card--front { left: 73px; background: var(--forest); color: var(--stone); }
  .card--back { left: 615px; background: var(--stone); color: var(--ink); }

  .brand {
    position: absolute;
    top: 0;
    bottom: 0;
    display: flex;
    flex-direction: column;
    align-items: center;
    justify-content: center;
    gap: 8px;
  }
  .brand__lockup {
    display: flex;
    align-items: center;
    gap: 10px;
    white-space: nowrap;
  }
  .brand__dot {
    width: 12px;
    height: 12px;
    border-radius: 50%;
    flex: none;
    background: currentColor;
  }
  .brand__name {
    font-weight: 400;
    line-height: 1.1;
    letter-spacing: 0.3px;
  }
  .brand__tagline {
    font-weight: 400;
    letter-spacing: 1.4px;
    text-transform: uppercase;
    white-space: nowrap;
  }

  .card--front .brand { left: 0; right: 0; }
  .card--front .brand__name { font-size: 30px; }
  .card--front .brand__tagline { font-size: 11px; }

  .card--back .brand { left: 14px; width: 230px; color: var(--forest); }
  .card--back .brand__dot { width: 9px; height: 9px; }
  .card--back .brand__name { font-size: 21px; }
  .card--back .brand__tagline { font-size: 8.5px; letter-spacing: 1px; }

  .divider {
    position: absolute;
    left: 257px;
    top: 37px;
    width: 1.5px;
    height: 221px;
    background: var(--rule);
  }
  .contact {
    position: absolute;
    left: 286px;
    top: 68px;
    font-size: 12.5px;
    line-height: 1.38;
  }
  .contact__name {
    font-weight: 700;
    font-size: 16px;
    letter-spacing: 0.2px;
  }
  .contact__role {
    font-weight: 700;
    font-size: 11px;
    letter-spacing: 0.3px;
    margin-bottom: 14px;
  }
  .contact__address { font-style: normal; margin-bottom: 14px; }
  .contact__web { margin-top: 12px; }
</style>
</head>
<body>
<main class="canvas">
  <section class="card card--front" aria-label="Business card front">
    <div class="brand">
      <div class="brand__lockup">
        <span class="brand__dot" aria-hidden="true"></span>
        <span class="brand__name">Thistlecove Gardens</span>
      </div>
      <p class="brand__tagline">Landscape and Garden Design</p>
    </div>
  </section>

  <section class="card card--back" aria-label="Business card back">
    <div class="brand">
      <div class="brand__lockup">
        <span class="brand__dot" aria-hidden="true"></span>
        <span class="brand__name">Thistlecove Gardens</span>
      </div>
      <p class="brand__tagline">Landscape and Garden Design</p>
    </div>
    <div class="divider" aria-hidden="true"></div>
    <div class="contact">
      <p class="contact__name">MARLOW PENHALIGON</p>
      <p class="contact__role">MANAGING DIRECTOR</p>
      <address class="contact__address">48 Aspen Ridge Road<br>Boulder, Colorado 80302</address>
      <p class="contact__phone">555 214 08 37</p>
      <p class="contact__email">info@thistlecovegardens.com</p>
      <p class="contact__web">www.thistlecovegardens.com</p>
    </div>
  </section>
</main>
</body>
</html>
```